San Francisco Leading Consulting firm - 47Nova Web Design Project

•Create a Web Design
•Uncoded webpage layout design
•2 Pages Design - Homepage + Interior Page

Task Description
Hello, we're looking for a re-design our current website www.47nova-example.com

we have a sample mockup design @

http://47nova.civicpane-example.org/

This shows the layout that we like and also a sample of 6 pictures that would change based on where you mouse over..

6 pictures HOME design needs to be included.

SMART
THOUGHTFUL
FLEXIBLE
CREATIVE SERVICES
TECHNICAL SERVICES
PARTNERS

sites we like:

http://www.brelmoradvisory-example.com/Home.cfm?id=Home
http://www.pixelquarry-example.com/index.html

Our company can be best described as: 100+ employees, cutting-edge, depandable, innovative, strong, smart.

Our Primary focus is: IT Consulting Services and Creative Design services

47Nova LLC is a consulting firm providing creative design, business and technology solutions to both private and public interests.

Established in 1996, 47Nova is a San Francisco based company providing specialists for a range of business needs including:

Creative Design Services
•Print
•Logo Design
•Website Design
•Illustration

and

Business and Technology solutions

•Application Software and Web Development
•Business Process Re-Design (BPR)
•Business/Systems Analysis and Requirement Documentation
•Mentoring and Training
•Network/Hardware Installation Services
•System Design and Architecture
•Vendor Management
•Teamvault Architecture and Implementation

our sample mockup site:

Reason: Due to holiday season, we're not available to work with designers and finilize our design.  

Thank you very much for submitting your design.

We appreciate your time and creativity.   Since, our office is currently closed for holidays, we will be reviewing it in details next week and will make our decision as soon as possible.

It would be great if you could submit any of your changes by Wed next week, so it would be part of our reviews. 

Please see updated wireframe under attachments:  we have some minor updates to our wireframe that we would like you to update your designs, if possible.  

We also encorouge you not to use our standard wireframe and come up with more unique designs.   Everything would be considered when we review your design.

 

Target Market(s)

Creative services and professional services clients, including government agencies

Industry/Entity Type

Business

Requirements
Must have
• Clean, professional look, easy navigation

```html
<!DOCTYPE html>
<html lang="en">
<head>
<meta charset="utf-8">
<title>47Nova — IT Consulting &amp; Creative Services</title>
<link rel="stylesheet" href="https://fonts.googleapis.com/css2?family=Oswald:wght@500&family=Arimo:wght@400;700&family=Alfa+Slab+One&family=Ubuntu:wght@400&display=swap">
<style>
:root{
  --page-deep:#0b3a72;
  --page-mid:#1d5595;
  --page-light:#5d8cc0;
  --sheet:#ffffff;
  --hero-light:#7fc0e2;
  --hero-mid:#3f93bf;
  --hero-dark:#1d6e98;
  --nav-top:#56acd2;
  --nav-bottom:#1e7aa6;
  --nav-active:#165f83;
  --heading:#585a70;
  --body-text:#4a4a56;
  --link:#1a8ac6;
  --muted:#9a9aac;
  --rule:#b9b9c6;
  --button-dark:#0f4c6e;
  --button-light:#2a7ea6;
}
*{box-sizing:border-box;margin:0;padding:0}
html,body{width:1200px;height:924px;overflow:hidden}
body{
  position:relative;
  font-family:"Arimo",Arial,sans-serif;
  color:var(--body-text);
  background:radial-gradient(ellipse 700px 600px at 600px 300px,var(--page-light) 0%,var(--page-mid) 45%,var(--page-deep) 100%);
}
a{color:var(--link);text-decoration:none}
.abs{position:absolute}

.sheet{position:absolute;left:181px;top:0;width:822px;height:840px;background:var(--sheet);box-shadow:0 0 18px rgba(0,0,0,.25)}

/* header */
.brand{left:199px;top:38px;display:flex;align-items:center;gap:10px}
.brand-dot{width:30px;height:30px;border-radius:50%;background:#2a8fd0}
.brand-name{font-family:"Ubuntu",sans-serif;font-size:32px;color:#2b2b33;letter-spacing:2px}
.main-nav{left:518px;top:0;width:458px;height:28px;border-radius:0 0 12px 12px;
  background:linear-gradient(var(--nav-top),var(--nav-bottom));display:flex;padding-left:38px}
.main-nav a{color:#fff;font-size:12.5px;line-height:28px;padding:0 10px}
.main-nav a.current{background:var(--nav-active);box-shadow:inset 1px 0 rgba(255,255,255,.25),inset -1px 0 rgba(255,255,255,.25)}
.call-pill{left:728px;top:54px;width:245px;height:23px;border-radius:12px;background:#efeff1;
  font-family:"Ubuntu",sans-serif;font-size:14px;color:#333;line-height:23px;text-align:center}

/* hero */
.hero{left:192px;top:108px;width:801px;height:305px;border:1px solid #1a6890;
  background:radial-gradient(ellipse 420px 260px at 150px 0,var(--hero-light) 0%,var(--hero-mid) 55%,var(--hero-dark) 100%)}
.hero-title{left:220px;top:156px;font-family:"Oswald",sans-serif;font-size:27px;color:#fff;letter-spacing:-.3px;transform:scaleX(.85);transform-origin:left}
.hero-copy{left:220px;top:201px;width:325px;font-size:11.9px;line-height:20.5px;letter-spacing:-.15px;color:#fff}
.hero-button{left:220px;top:339px;width:151px;height:38px;border-radius:7px;
  background:linear-gradient(var(--button-light),var(--button-dark));box-shadow:0 2px 3px rgba(0,0,0,.3);
  color:#fff;font-weight:700;font-size:13.5px;line-height:38px;text-align:center}
.slide-card{background:#fff;box-shadow:0 2px 6px rgba(0,0,0,.35)}
.slide-photo{left:559px;top:146px;width:406px;height:222px;background:linear-gradient(160deg,#9a9a9a 0%,#3a3a3a 45%,#111 75%,#6a6a6a 100%)}
.slide-band{left:559px;top:211px;width:406px;height:90px;background:rgba(0,0,0,.45)}
.slide-word{left:559px;top:214px;width:406px;text-align:center;font-family:"Alfa Slab One",serif;font-size:36px;color:#fff}
.slide-tag{left:559px;top:255px;width:406px;text-align:center;font-family:"Oswald",sans-serif;font-size:14.5px;line-height:20px;color:#fff}
.slide-arrow{width:34px;height:34px;border-radius:50%;background:linear-gradient(#fff,#d6d6d6);box-shadow:0 1px 3px rgba(0,0,0,.4)}
.hero-shadow{left:192px;top:413px;width:801px;height:12px;background:linear-gradient(rgba(0,0,0,.08),transparent)}

/* content */
.section-title{font-family:"Oswald",sans-serif;font-size:26px;color:var(--heading);transform:scaleX(.82);transform-origin:left;letter-spacing:-.3px}
.thumb{width:68px;height:68px}
.copy{font-size:10.5px;line-height:18px}
.sub-title{font-weight:700;font-size:11.5px;color:#3f3f4a}
.more::after{content:" →"}
.news-title{font-size:14px;line-height:17px;color:var(--link)}
.news-date{font-size:8.5px;color:var(--muted)}
.dots{width:200px;border-top:1px dotted var(--rule)}
.partner-strip{left:220px;top:703px;width:506px;height:70px;border:1px solid #e2e2e6;background:linear-gradient(#fff,#f1f1f3)}
.partner-badge{position:absolute;top:14px;width:56px;height:42px;border-radius:6px;background:#d7dde6}
.strip-arrow{width:20px;height:20px;border-radius:50%;background:linear-gradient(#fff,#ddd);box-shadow:0 1px 2px rgba(0,0,0,.35)}

/* footer */
.footer-line{left:0;width:1200px;text-align:center;color:#e6eef8;font-size:10.5px}
.footer-nav a{color:#e6eef8;margin:0 6px}
.footer-nav span{color:#9fbde0}
</style>
</head>
<body>
<div class="sheet"></div>

<header>
  <div class="abs brand"><span class="brand-dot"></span><span class="brand-name">47Nova</span></div>
  <nav class="abs main-nav">
    <a class="current" href="#">Home</a><a href="#">Company</a><a href="#">Services</a><a href="#">Partners</a><a href="#">Contact</a><a href="#">Login</a>
  </nav>
  <div class="abs call-pill">Call Us Now on 1-415-555-0147</div>
</header>

<section>
  <div class="abs hero"></div>
  <div class="abs hero-shadow"></div>
  <h1 class="abs hero-title">WELCOME TO 47NOVA</h1>
  <p class="abs hero-copy">47Nova provides professional experience in all phases of IT projects from vendor selection to post production support. We assist our clients not only in their IT solutions, but also provide professional services such as transitioning with conversion activities, Business Process Reengineering (BPR), training and business support.</p>
  <a class="abs hero-button" href="#">View Our Services</a>

  <div class="abs slide-card" style="left:550px;top:130px;width:425px;height:250px;transform:rotate(-3deg)"></div>
  <div class="abs slide-card" style="left:550px;top:138px;width:424px;height:240px;transform:rotate(1.5deg)"></div>
  <div class="abs slide-card" style="left:554px;top:141px;width:416px;height:233px"></div>
  <div class="abs slide-photo" role="img" aria-label="Black and white photo of a hand moving a chess piece on a board"></div>
  <div class="abs slide-band"></div>
  <div class="abs slide-word">SMART</div>
  <div class="abs slide-tag">WE DON’T BELIEVE IN THE TERM<br>“OVERQUALIFIED.”</div>
  <svg class="abs slide-arrow" style="left:539px;top:234px" viewBox="0 0 34 34"><path d="M20 11 L12 17 L20 23Z" fill="#a9a9a9"/></svg>
  <svg class="abs slide-arrow" style="left:950px;top:234px" viewBox="0 0 34 34"><path d="M14 11 L22 17 L14 23Z" fill="#a9a9a9"/></svg>
</section>

<main>
  <h2 class="abs section-title" style="left:220px;top:440px">TECHNICAL SERVICES</h2>
  <div class="abs thumb" style="left:220px;top:485px;background:linear-gradient(135deg,#ddd,#444 70%,#222)" role="img" aria-label="Photo of a hand typing on a keyboard"></div>
  <p class="abs copy" style="left:303px;top:481px;width:160px">47Nova's team has expertise in most databases, operating systems, programming languages and platforms currently used by</p>
  <p class="abs copy" style="left:220px;top:561px;width:245px">government. We also excel in providing consultants for IT and non-IT services, as well as staff augmentation and placement services.<br><a class="more" href="#">Learn More</a></p>

  <h2 class="abs section-title" style="left:494px;top:440px">CREATIVE SERVICES</h2>
  <div class="abs thumb" style="left:494px;top:485px;background:linear-gradient(160deg,#e04a4a,#a01818 60%,#1c5a8a)" role="img" aria-label="Holiday greeting card design with a child in a winter hat"></div>
  <p class="abs sub-title" style="left:577px;top:482px">The 47Nova Difference</p>
  <p class="abs copy" style="left:577px;top:504px;width:160px">Smart, Flexible, Thoughtful: Find out why leading corporations and government agencies are turning</p>
  <p class="abs copy" style="left:494px;top:561px;width:240px">to 47nova to help manage their most demanding IT services challenges.<br><a class="more" href="#">View Portfolio</a></p>

  <h2 class="abs section-title" style="left:769px;top:440px">LATEST NEWS</h2>
  <a class="abs news-title" style="left:769px;top:481px" href="#">Lorem Ipsum Dolor Sit Amet</a>
  <p class="abs news-date" style="left:769px;top:498px">30 November, 2010</p>
  <p class="abs copy" style="left:769px;top:514px;width:205px">Cras scelerisque, felis nec sagittis mollis, mi libero lobortis nibh, vel consectetur magna justo quis enim. <a class="more" href="#">More</a></p>
  <div class="abs dots" style="left:769px;top:582px"></div>
  <a class="abs news-title" style="left:769px;top:596px;width:200px" href="#">Donec tristique justo sed arcu rhoncus laoreet</a>
  <p class="abs news-date" style="left:769px;top:630px">28 November, 2010</p>
  <p class="abs copy" style="left:769px;top:646px;width:205px">Lulla vehicula purus non est porta euismod pellentesque leo tincidunt. Donec lacinia purus. <a class="more" href="#">More</a></p>
  <div class="abs dots" style="left:769px;top:713px"></div>
  <a class="abs copy more" style="left:769px;top:720px" href="#">Go to Blog</a>

  <h2 class="abs section-title" style="left:220px;top:659px">OUR PARTNERS</h2>
  <div class="abs partner-strip">
    <span class="partner-badge" style="left:20px"></span>
    <span class="partner-badge" style="left:90px"></span>
    <span class="partner-badge" style="left:172px"></span>
    <span class="partner-badge" style="left:256px"></span>
    <span class="partner-badge" style="left:335px"></span>
    <span class="partner-badge" style="left:413px"></span>
  </div>
  <svg class="abs strip-arrow" style="left:213px;top:728px" viewBox="0 0 20 20"><path d="M12 6 L7 10 L12 14Z" fill="#aaa"/></svg>
  <svg class="abs strip-arrow" style="left:715px;top:728px" viewBox="0 0 20 20"><path d="M8 6 L13 10 L8 14Z" fill="#aaa"/></svg>
  <a class="abs copy more" style="left:220px;top:775px" href="#">Learn More</a>
</main>

<footer>
  <p class="abs footer-line" style="top:848px">Copyright © 2010. &nbsp; 47Nova, LLC. &nbsp; All rights reserved.</p>
  <p class="abs footer-line footer-nav" style="top:864px"><a href="#">Home</a><span>•</span><a href="#">About</a><span>•</span><a href="#">Services</a><span>•</span><a href="#">Partners</a><span>•</span><a href="#">Contact</a><span>•</span><a href="#">Help &amp; F.A.Q</a></p>
</footer>
</body>
</html>
```